Tobias Wrenfield - Cinematographer

NEED:
I'm looking for a sleek, professional, modern business card that will give give the recipient the impression that they can trust their production will go smoothly by hiring me. I will bring creativity and knowledge to their shoot, so that we can create powerful images.
I am looking for a card with a strong style and design ethos that could be expanded to a website and a full visual/graphic/design entity for me.
ABOUT ME:
I am a mid-twenties cinematographer, I work on music video, narrative short, commercial, and corporate projects. I blend the science and artistry of cameras and filmmaking to tell a story. I'm an artist, a technician, and a manager.
DESIGN:
I like sleek, simple design. Black, dark grays, white, dark navy, steel blues, I love cyan, but also cyan and red. I am not a fan of earthy tones. I generally prefer modern, san-serif fonts over serifs. My old logo was based on an aperture, a multi-blade device at the back of a lens that controls how much light passes through, but I made it with so many colors, that it doesn't necessarily lend itself to a specific color-scheme or design ethos. I liked that the aperture design provided a sense of the technical requirements of my job. I'm a fan of matte business cards, but am open to plenty of specialty print processes to make an outstanding card.
ATTACHED FILES:
My Old Rainbox Aperture Logo, plus a few designs I've tried playing around with, but am not tied to. I AM OPEN TO NEW DESIGNS, DO NOT FEEL TIED TO THIS.
**I've pulled my old logo down from the attached files, and instead attached other business cards I like, so as not to mislead you where I would like to go.
INFO:
Name: Tobias Wrenfield
Job: Cinematographer
Email: tkwrenfield@quillbox.example
Phone: 503.618.2907
Website: tobiaswrenfield.example
Updates
I'm adding some images of other cards that I like, and removing my old logo, since I'm looking for something new, and don't want that old logo to push anyone a certain direction.

```html
<!DOCTYPE html>
<html lang="en">
<head>
<meta charset="utf-8">
<title>Tobias Wrenfield — Cinematographer Business Card</title>
<link rel="stylesheet" href="https://fonts.googleapis.com/css2?family=Oswald:wght@500;700&family=Jost:wght@300&display=swap">
<style>
  :root {
    --backdrop: #1c1c1e;
    --card-light: #ececec;
    --card-dark: #141414;
    --ink: #111111;
    --ink-soft: #555555;
    --name-muted: #6a6a6a;
    --name-bright: #f2f2f2;
    --mark-dark: #161616;
    --mark-light: #e4e4e4;
    --caption: #bdbdbd;
  }
  html, body {
    margin: 0;
    width: 1200px;
    height: 800px;
    overflow: hidden;
    background: var(--backdrop);
  }
  .stage {
    width: 1200px;
    height: 800px;
    display: flex;
    align-items: center;
    justify-content: center;
    gap: 60px;
  }
  .card {
    position: relative;
    width: 525px;
    height: 300px;
    border-radius: 14px;
    overflow: hidden;
    box-shadow: 0 12px 30px rgba(0,0,0,0.45);
  }
  .card--front { background: var(--card-light); }
  .card--back { background: var(--card-dark); }

  .brand-mark {
    position: absolute;
    border-radius: 50%;
  }
  .card--front .brand-mark {
    width: 150px; height: 150px;
    left: 188px; top: 40px;
    background: var(--mark-dark);
  }
  .card--front .brand-name {
    position: absolute;
    left: 0; right: 0; top: 200px;
    text-align: center;
    font-family: "Jost", sans-serif;
    font-weight: 300;
    font-size: 15px;
    letter-spacing: 0.12em;
    color: var(--ink);
  }
  .contact-line {
    position: absolute;
    left: 26px; bottom: 26px;
    margin: 0;
    font-family: "Jost", sans-serif;
    font-weight: 300;
    font-size: 12.5px;
    letter-spacing: 0.03em;
    color: var(--ink-soft);
    white-space: nowrap;
  }
  .contact-line .sep { margin: 0 6px; }

  .card--back .brand-mark {
    width: 175px; height: 175px;
    left: 45px; top: 40px;
    background: var(--mark-light);
    box-shadow: 0 0 18px rgba(255,255,255,0.35);
  }
  .identity {
    position: absolute;
    right: 30px; top: 170px;
    text-align: right;
  }
  .identity__name {
    margin: 0;
    font-family: "Oswald", sans-serif;
    font-size: 34px;
    line-height: 1;
    letter-spacing: 0.06em;
    text-transform: uppercase;
  }
  .identity__first { font-weight: 500; color: var(--name-muted); }
  .identity__last { font-weight: 700; color: var(--name-bright); }
  .identity__role {
    margin: 6px 0 0;
    font-family: "Jost", sans-serif;
    font-weight: 300;
    font-size: 14px;
    letter-spacing: 0.04em;
    color: var(--caption);
  }
</style>
</head>
<body>
<main class="stage">
  <section class="card card--front" aria-label="Card front">
    <div class="brand-mark"></div>
    <div class="brand-name">Tobias Wrenfield</div>
    <p class="contact-line">tkwrenfield@quillbox.example<span class="sep">|</span>503.618.2907<span class="sep">|</span>tobiaswrenfield.example</p>
  </section>

  <section class="card card--back" aria-label="Card back">
    <div class="brand-mark"></div>
    <div class="identity">
      <h1 class="identity__name"><span class="identity__first">Tobias</span> <span class="identity__last">Wrenfield</span></h1>
      <p class="identity__role">Cinematographer</p>
    </div>
  </section>
</main>
</body>
</html>
```